Business card design Needed for new logo / Construction business, home extensions and new builds

We need a business card design using our new logo files which i will attach to this project :)

We are a small construction business specialising in home extensions, new builds and property development. We are very ambitious and would appreciate professional and elegant designs for our new business card.

Very serious about using the services on BriefNest and recently acquired our new logo from here :)

Please get involved, i will feedback when i can as i am very busy but can respond daily, thanks

Target Market(s)

People that want to build onto their houses, new building developments or adding too their existing property

Industry/Entity Type

Construction

Contact Information for Business Card

Hollin Marsh Construction, Tobias Renwick (Managing Director), Tel 07822200444, email - info@hollin-marsh, www.hollin-marsh.co.uk

Colors

Designer to choose colors to be used in the design.

Requirements
Must have
• I like a deep grey on the back please. A lot of you have provided black from and back, try mixing things up a little. The black looks cool 😎 Thanks

```html
<!DOCTYPE html>
<html lang="en">
<head>
<meta charset="utf-8">
<title>Hollin Marsh Construction – Business Card</title>
<link rel="stylesheet" href="https://fonts.googleapis.com/css2?family=Cinzel:wght@600&family=Poppins:wght@400&display=swap">
<style>
  :root {
    --canvas: #5b5b5b;
    --card-black: #000000;
    --card-deep-grey: #262626;
    --gold-dark: #a96c03;
    --gold-light: #f8cf82;
    --gold-mark: #d9a440;
    --silver-dark: #8f9397;
    --silver-light: #eef0f2;
    --ink: #111111;
  }
  * { box-sizing: border-box; margin: 0; padding: 0; }
  html, body { width: 1200px; height: 1112px; overflow: hidden; }
  body { background: var(--canvas); position: relative; }

  .card {
    position: absolute;
    left: 255px;
    width: 654px;
    height: 404px;
    background: var(--card-black);
    box-shadow: 0 2px 8px rgba(0,0,0,.35);
    overflow: hidden;
  }
  .card--front { top: 134px; }
  .card--back { top: 560px; background: var(--card-deep-grey); }

  .front-brand {
    position: absolute; left: 0; top: 0;
    width: 325px; height: 404px;
  }
  .divider {
    position: absolute; left: 325px; top: 0;
    width: 6px; height: 404px;
    background: linear-gradient(180deg, var(--silver-dark), var(--silver-light) 50%, var(--silver-dark));
  }
  .details {
    position: absolute; left: 331px; top: 0;
    width: 323px; height: 404px;
    background: linear-gradient(180deg, var(--gold-dark) 0%, #d5a553 28%, var(--gold-light) 52%, #d4a24e 76%, var(--gold-dark) 100%);
    color: var(--ink);
    font-family: 'Poppins', sans-serif;
  }

  .brand {
    position: absolute; left: 0; right: 0;
    text-align: center;
    font-family: 'Cinzel', serif;
    font-weight: 600;
    color: var(--gold-mark);
    white-space: nowrap;
  }
  .brand__square {
    display: block; margin: 0 auto;
    background: var(--gold-mark);
  }
  .brand__name { display: block; line-height: 1; }
  .brand__sub { display: block; line-height: 1; }

  .front-brand .brand { top: 110px; }
  .front-brand .brand__square { width: 80px; height: 80px; margin-bottom: 60px; }
  .front-brand .brand__name { font-size: 34px; }
  .front-brand .brand__sub { font-size: 21.5px; margin-top: 2px; }

  .card--back .brand { top: 120px; }
  .card--back .brand__square { width: 90px; height: 90px; margin-bottom: 46px; }
  .card--back .brand__name { font-size: 37px; }
  .card--back .brand__sub { font-size: 23px; margin-top: 0; }

  .chevron { position: absolute; left: 0; top: 96px; width: 20px; height: 38px; }

  .person__name {
    position: absolute; left: 28px; top: 93px;
    font-family: 'Cinzel', serif; font-weight: 600;
    font-size: 26px; letter-spacing: 0.4px; line-height: 1;
  }
  .person__title {
    position: absolute; left: 28px; top: 126px;
    font-size: 19px; line-height: 1;
  }
  .contact-list {
    position: absolute; left: 30px; top: 172px;
    list-style: none; font-size: 19px; line-height: 24px;
  }
  .contact-list li { display: flex; align-items: center; }
  .contact-list svg { width: 17px; height: 17px; margin-right: 6px; flex: none; }
  .address {
    position: absolute; left: 30px; top: 259px;
    font-size: 19px; line-height: 24px; font-style: normal;
  }
</style>
</head>
<body>

<section class="card card--front">
  <div class="front-brand">
    <div class="brand">
      <span class="brand__square"></span>
      <span class="brand__name">HOLLIN MARSH</span>
      <span class="brand__sub">CONSTRUCTION</span>
    </div>
  </div>
  <div class="divider"></div>
  <div class="details">
    <svg class="chevron" viewBox="0 0 20 38" aria-hidden="true">
      <polyline points="1,2 18,19 1,36" fill="none" stroke="#f4f4f4" stroke-width="3"/>
    </svg>
    <h1 class="person__name">TOBIAS RENWICK</h1>
    <p class="person__title">Managing Director</p>
    <ul class="contact-list">
      <li>
        <svg viewBox="0 0 24 24" aria-hidden="true"><path d="M6.6 10.8a15.1 15.1 0 0 0 6.6 6.6l2.2-2.2c.3-.3.7-.4 1-.2 1.1.4 2.3.6 3.6.6.6 0 1 .4 1 1V20c0 .6-.4 1-1 1C10.6 21 3 13.4 3 4c0-.6.4-1 1-1h3.5c.6 0 1 .4 1 1 0 1.3.2 2.5.6 3.6.1.3 0 .7-.2 1z" fill="#111"/><path d="M14 3a7 7 0 0 1 7 7M14 6.5a3.5 3.5 0 0 1 3.5 3.5" fill="none" stroke="#111" stroke-width="2"/></svg>
        07822200444
      </li>
      <li>
        <svg viewBox="0 0 24 24" aria-hidden="true"><rect x="2" y="5" width="20" height="14" fill="#111"/><polyline points="2,5 12,13 22,5" fill="none" stroke="#e8bd6c" stroke-width="1.6"/></svg>
        info@hollin-marsh
      </li>
      <li>
        <svg viewBox="0 0 24 24" aria-hidden="true"><circle cx="12" cy="12" r="9.5" fill="none" stroke="#111" stroke-width="2"/><ellipse cx="12" cy="12" rx="4" ry="9.5" fill="none" stroke="#111" stroke-width="1.6"/><line x1="2.5" y1="12" x2="21.5" y2="12" stroke="#111" stroke-width="1.6"/><line x1="4" y1="7.5" x2="20" y2="7.5" stroke="#111" stroke-width="1.4"/><line x1="4" y1="16.5" x2="20" y2="16.5" stroke="#111" stroke-width="1.4"/></svg>
        www.hollin-marsh.co.uk
      </li>
    </ul>
    <address class="address">421, Address line name<br>goes here 45452,Country</address>
  </div>
</section>

<section class="card card--back">
  <div class="brand">
    <span class="brand__square"></span>
    <span class="brand__name">HOLLIN MARSH</span>
    <span class="brand__sub">CONSTRUCTION</span>
  </div>
</section>

</body>
</html>
```